Business Card Design and Stationary design for consulting firm

Harbourline Sourcing are looking for a new business card design and a design for their A4 letterhead / A4 invoices.

We are seeking to heavily increase our brand awareness and require a business card that's professional in appearance but also shows flare and innovation. A card design that people will remember.

About Us
Harbourline Sourcing are `The Sourcing Crew’.
Our mission is to be one of Australia’s greatest companies. Our aim is to help our customers achieve the best result from their purchasing experience.

Our Requirement:
• IMPACT! IMPACT! IMPACT!
• BUSINESS & PROFESSIONAL LOOKING

• Our business colours are orange, blue and green (See the logo attached).

We have provided an Art Design specification (attached) that needs to be followed for you to win the design. This also has the font, which is used on the logo.

We are after a two sided business card

Side One should have the:
The company Logo
The Sourcing Crew
www.harbourlinesourcing.com.au
Procure | Personnel | Probity & Privacy
Sydney | Melbourne | Adelaide | Brisbane

Side Two
Logo (optional)
Harbourline Sourcing (optional)
Employee details (details listed below)

The above format is our preferred option, but if you think you can come up with something better, feel free to put it forward.

We are leaving the design up to you, but it must incorporate the logo.

We will need a template that we can change the employee details on, as we will be adding more staff over the coming months.

The details below are for one employee per card with the same design.
------------------------

Employee Details:

Marcus Del Arroyo MBA, MMgmtStratProc
Principal Consultant
0491 372 618
Marcus@harbourlinesourcing.com.au

Brianna Tolley
Consulting Manager
0462 915 308
Brianna@harbourlinesourcing.com.au

Our website is www.harbourlinesourcing.com.au

The Letterhead / invoice needs to incorporate:
the company Logo
The Sourcing Crew
Sydney | Melbourne | Adelaide | Brisbane but otherwise the design is over to you.

This file needs to be delivered in word format as other detail will be added to the documents.

We look forward to you award winning designs. If you require any further information please feel free to contact us.

Regards
Harbourline Sourcing

Target Market(s)

Our Target market is companies with 80+ employees. The market we segment is heavily male based, between the ages of 35-55 years of age.

Industry/Entity Type

Consulting

Contact Information for Business Card

See Project Description

Font styles to use
Other font styles liked:
• See Art Specification

Requirements
Must have
• Company Colours, See Project Description
Should not have
• Be outside the Art specification guidelines

```html
<!DOCTYPE html>
<html lang="en">
<head>
<meta charset="utf-8">
<title>Harbourline Sourcing — Business Cards</title>
<link href="https://fonts.googleapis.com/css2?family=Lato:wght@400;700;900&display=swap" rel="stylesheet">
<style>
  :root {
    --page: #2a2a2a;
    --card: #141414;
    --card-edge: #1c1c1c;
    --map-tone: #1e2a36;
    --band: #1c9ad6;
    --band-dark: #1484bb;
    --ink: #f2f2f2;
    --ink-soft: #cfcfcf;
    --orange: #f07a1f;
    --green: #5bb531;
    --blue: #1c9ad6;
    --divider: #8a8a8a;
  }
  * { margin: 0; padding: 0; box-sizing: border-box; }
  html, body {
    width: 1200px; height: 873px; overflow: hidden;
    background: var(--page);
    font-family: "Lato", Arial, sans-serif;
  }
  .sheet {
    width: 1200px; height: 873px;
    display: flex; flex-direction: column; align-items: center; justify-content: center;
    gap: 25px;
  }
  .card {
    position: relative;
    width: 700px; height: 400px;
    background: var(--card);
    overflow: hidden;
    box-shadow: 0 10px 30px rgba(0,0,0,.5);
  }
  .world-map {
    position: absolute;
    left: 140px; top: 30px; width: 520px; height: 290px;
    background: radial-gradient(ellipse at 50% 45%, var(--map-tone) 0%, rgba(30,42,54,.35) 55%, transparent 75%);
    opacity: .8;
  }
  .band {
    position: absolute; left: 0; right: 0; bottom: 0; height: 56px;
    background: linear-gradient(180deg, var(--band), var(--band-dark));
    display: flex; align-items: center; justify-content: center;
    color: #fff; font-weight: 700;
  }
  .brand {
    display: flex; align-items: center; gap: 14px;
    color: var(--ink);
  }
  .brand-dot {
    width: 46px; height: 46px; border-radius: 50%;
    background: var(--orange);
    flex: none;
  }
  .brand-name {
    font-weight: 900; font-size: 34px; line-height: 1.02;
    letter-spacing: 1px; text-transform: uppercase;
  }

  /* Front */
  .card-front .brand { position: absolute; left: 180px; top: 82px; }
  .services {
    position: absolute; left: 200px; top: 232px;
    color: var(--ink-soft); font-size: 17px; line-height: 1.6;
  }
  .card-front .band { font-size: 20px; letter-spacing: 6px; text-transform: uppercase; }

  /* Back */
  .card-back .brand { position: absolute; left: 70px; top: 148px; }
  .card-back .brand-name { font-size: 28px; }
  .divider {
    position: absolute; left: 348px; top: 70px; width: 2px; height: 220px;
    background: linear-gradient(180deg, transparent, var(--divider) 30%, var(--divider) 70%, transparent);
  }
  .details { position: absolute; left: 380px; top: 78px; }
  .person-name { color: var(--orange); font-weight: 700; font-size: 24px; }
  .person-role { color: var(--ink); font-size: 17px; margin-top: 4px; }
  .contact-list { list-style: none; margin-top: 52px; }
  .contact-list li {
    display: flex; align-items: center; gap: 10px;
    color: var(--ink); font-size: 17px; margin-bottom: 14px;
  }
  .contact-icon { width: 26px; height: 26px; flex: none; }
  .card-back .band { font-size: 22px; letter-spacing: .5px; }
</style>
</head>
<body>
<main class="sheet">

  <section class="card card-front" aria-label="Business card front">
    <div class="world-map" role="img" aria-label="Dotted world map background"></div>
    <div class="brand">
      <span class="brand-dot"></span>
      <span class="brand-name">Harbourline<br>Sourcing</span>
    </div>
    <p class="services">Procure | Personnel | Probity &amp; Privacy<br>Sydney | Melbourne | Adelaide | Brisbane</p>
    <div class="band">The Sourcing Crew</div>
  </section>

  <section class="card card-back" aria-label="Business card back">
    <div class="world-map" role="img" aria-label="Dotted world map background"></div>
    <div class="brand">
      <span class="brand-dot"></span>
      <span class="brand-name">Harbourline<br>Sourcing</span>
    </div>
    <div class="divider"></div>
    <div class="details">
      <p class="person-name">Brianna Tolley</p>
      <p class="person-role">Consulting Manager</p>
      <ul class="contact-list">
        <li>
          <svg class="contact-icon" viewBox="0 0 26 26" aria-hidden="true">
            <circle cx="13" cy="13" r="13" fill="var(--green)"/>
            <path d="M9 7.5c.6-.4 1.3-.3 1.7.3l1.2 1.8c.3.5.2 1.1-.2 1.5l-.8.7c.6 1.4 1.8 2.6 3.2 3.2l.7-.8c.4-.4 1-.5 1.5-.2l1.8 1.2c.6.4.7 1.1.3 1.7l-.6.8c-.5.6-1.3.9-2.1.7-3.4-.9-6.1-3.6-7-7-.2-.8.1-1.6.7-2.1z" fill="#fff"/>
          </svg>
          0462 915 308
        </li>
        <li>
          <svg class="contact-icon" viewBox="0 0 26 26" aria-hidden="true">
            <circle cx="13" cy="13" r="13" fill="var(--blue)"/>
            <rect x="6.5" y="8.5" width="13" height="9" rx="1" fill="#fff"/>
            <path d="M6.8 9l6.2 4.8L19.2 9" fill="none" stroke="var(--blue)" stroke-width="1.3"/>
          </svg>
          Brianna@harbourlinesourcing.com.au
        </li>
      </ul>
    </div>
    <div class="band">www.harbourlinesourcing.com.au</div>
  </section>

</main>
</body>
</html>
```